Window Tinting Website Design

We are working with a Window Tinting company in California. They do commercial, residential, and automotive tint.

Some websites for inspiration:
https://www.velmoshadez.com/
https://www.qpridegleam.com/
https://drobfinishx.com/

Thank you for taking the time to consider designing a website for us. We are web developers based in Riverbend, CA, USA. Most of our projects go through the same process. Understanding this process may help you win a project with us. We custom-code all of our websites in-house. We don’t have any requirements as to what tools you use for your design, but we ask that you follow these guidelines.

IMAGES:
If you use any images or icons in the design, we ask that you have a link to the asset so we can purchase the image/icon. Most of the designs we submit do not have the customer’s images on them unless they have some great images. Be creative; show us the feeling you are trying to portray with your image choices. Use any royalty-free site you choose. We subscribe to Brenlo and mainly use their images, but we can purchase images outside of Brenlo. PLEASE NOTE: we will not submit designs to clients with watermarks on the images.

FONTS:
We ask that you identify the fonts you’re using in the design. This can be done in a message if you want. We typically use Google Fonts and Brenlo Fonts.

CONTENT:
We're always open to different content and ideas. We often submit designs with stock images so the client can see our vision. We typically take pictures after the website launch to use their images with our vision. Lorem Ipsum is fine for paragraphs, but we ask that you make the Headers with correct English. We want to be able to show the vision and identify the sections of the website.

INSPIRATION:
We typically add a couple of links in the brief of websites we like to help you get started in your design.

REVISIONS:
We do not often ask for revisions of the designs unless we see something in the design that may not appeal to the client. If there are slight changes that we want to make, we do that in the development process.

FEEDBACK:
We rarely give feedback on designs during the design process. We are working on many website projects and do not have the time to provide feedback. We usually respond if your request is well thought out and asks specific questions, but a note asking “feedback, please” usually goes unanswered.

```html
<!DOCTYPE html>
<html lang="en">
<head>
<meta charset="utf-8">
<title>Nova Shade Tinting — Window Tinting Experts</title>
<link rel="stylesheet" href="https://fonts.googleapis.com/css2?family=Outfit:wght@300;400;500;600&display=swap">
<style>
:root{
  --red:#c8102e;
  --ink:#0e0e0f;
  --panel:#222223;
  --card:#2f2f31;
  --line:#4a4a4d;
  --white:#ffffff;
  --muted:#b9b9bc;
  --star:#f2b705;
}
*{box-sizing:border-box;margin:0;padding:0}
html,body{width:1200px;height:5000px;overflow:hidden}
body{background:var(--ink);color:var(--white);font-family:"Outfit",sans-serif;position:relative}
.abs{position:absolute}
.shape{position:absolute;left:0;width:1200px}
.ghost{position:absolute;font-weight:500;line-height:1;white-space:nowrap;letter-spacing:2px;color:rgba(255,255,255,.05)}
.ghost.red{color:rgba(200,16,46,.2)}
.btn{position:absolute;display:flex;align-items:center;justify-content:center;font-size:12px;font-weight:500;border-radius:6px;background:var(--red);color:var(--white);white-space:nowrap}
.btn.outline{background:transparent;border:2px solid var(--white)}
.photo{position:absolute;border-radius:4px}
.accent{color:var(--red)}
h2{position:absolute;font-weight:400;font-size:44px;line-height:1}
p.body{position:absolute;font-size:12.5px;line-height:1.7;color:var(--muted);font-weight:300}

/* header */
.nav a{position:absolute;top:32px;font-size:12px;font-weight:500;color:var(--white);text-decoration:none}
.brand{position:absolute;display:flex;align-items:center;gap:8px;font-size:15px;font-weight:600;color:var(--white);white-space:nowrap}
.brand .dot{width:22px;height:22px;border-radius:50%;background:var(--red)}

/* hero */
.hero-title{position:absolute;left:118px;top:146px;font-size:64px;font-weight:500;line-height:1.08;white-space:nowrap}
.contact{position:absolute;top:478px;display:flex;align-items:center;gap:14px}
.contact small{display:block;font-size:9px;letter-spacing:.5px;color:#f3d1d6}
.contact b{display:block;font-size:11px;font-weight:500;margin-top:6px;white-space:nowrap}

/* partners */
.partner{position:absolute;top:666px;font-size:21px;font-weight:500;color:#a5a5a8;transform:translateX(-50%)}

/* stats */
.stat{position:absolute;text-align:center;width:305px}
.stat .num{font-size:40px;font-weight:400}
.stat .lbl{font-size:17px;margin-top:18px;font-weight:300}

/* features */
.feature{position:absolute;top:2628px;width:260px;text-align:center;transform:translateX(-50%)}
.feature .ic{width:40px;height:40px;border-radius:50%;background:var(--red);margin:0 auto;display:flex;align-items:center;justify-content:center}
.feature span{display:block;margin-top:24px;font-size:16px;font-weight:300}

/* tabs */
.tabs{position:absolute;top:3140px;left:0;width:1200px;display:flex;justify-content:center;gap:24px;font-size:11px;color:#8e8e92}
.tabs .on{color:var(--white);border-bottom:2px solid var(--red);padding-bottom:6px}

/* reviews */
.review{position:absolute;width:286px;height:233px;background:var(--card);border-radius:6px;padding:24px 20px}
.review .stars{color:var(--star);font-size:14px;letter-spacing:3px}
.review q{display:block;margin-top:12px;font-size:11px;line-height:1.5;color:#e6e6e8;quotes:"\201C" "\201D"}
.review hr{border:0;border-top:1px solid #6a6a6e;margin:22px 0 18px}
.review .who{display:flex;align-items:center;gap:14px}
.review .av{width:32px;height:32px;border-radius:50%;background:linear-gradient(135deg,#7b6a5d,#3e3834)}
.review .who b{display:block;font-size:11px;font-weight:500}
.review .who small{display:block;font-size:9px;color:#9a9a9e;margin-top:2px}

/* footer */
.fcol h4{font-size:16px;font-weight:400;margin-bottom:24px}
.fcol a{display:block;font-size:11px;color:var(--white);text-decoration:none;margin-bottom:20px}
.social{position:absolute;top:4816px;width:36px;height:36px;border-radius:50%;background:var(--white);display:flex;align-items:center;justify-content:center}
</style>
</head>
<body>

<!-- HERO -->
<div class="photo" style="left:780px;top:0;width:420px;height:260px;border-radius:0;background:linear-gradient(200deg,#3a3a3d 0%,#1a1a1c 55%,var(--ink) 100%)" role="img" aria-label="Dark glass building facade"></div>
<div class="abs" style="left:0;top:94px;width:1200px;height:1px;background:#2f2f31"></div>

<svg class="shape" style="top:0" width="1200" height="620" aria-hidden="true">
  <polygon points="0,423 1200,369 1200,495 0,613" fill="var(--red)"/>
</svg>

<div class="photo" style="left:500px;top:238px;width:700px;height:232px;border-radius:0;background:radial-gradient(ellipse 48% 42% at 62% 52%,#9a9b9f 0%,#6f7074 35%,#3b3b3e 65%,rgba(30,30,32,0) 100%)" role="img" aria-label="Grey sports coupe with tinted windows"></div>

<div class="brand" style="left:118px;top:28px"><span class="dot"></span>Nova Shade Tinting</div>
<nav class="nav">
  <a style="left:518px">Automotive</a>
  <a style="left:641px">Commercial</a>
  <a style="left:766px">Residential</a>
  <a style="left:884px">About us</a>
</nav>
<div class="btn" style="left:942px;top:24px;width:140px;height:44px;border:2px solid #8a8a8e;background:#3a3a3d">Get a quote</div>

<div class="ghost red" style="left:0;top:130px;font-size:130px">EXPERTS</div>
<div class="hero-title">The window<br>tinting experts</div>
<div class="btn" style="left:118px;top:324px;width:142px;height:42px">Get a quote</div>

<div class="contact" style="left:118px">
  <svg width="18" height="18" viewBox="0 0 24 24" fill="none" stroke="#fff" stroke-width="2"><path d="M22 16.9v3a2 2 0 0 1-2.2 2 19.8 19.8 0 0 1-8.6-3.1 19.5 19.5 0 0 1-6-6A19.8 19.8 0 0 1 2.1 4.2 2 2 0 0 1 4.1 2h3a2 2 0 0 1 2 1.7c.1 1 .4 1.9.7 2.8a2 2 0 0 1-.5 2.1L8 9.9a16 16 0 0 0 6 6l1.3-1.3a2 2 0 0 1 2.1-.4c.9.3 1.8.6 2.8.7a2 2 0 0 1 1.7 2z"/></svg>
  <div><small>CALL US:</small><b>(209) 555-0148</b></div>
</div>
<div class="abs" style="left:251px;top:468px;width:1px;height:52px;background:rgba(255,255,255,.6)"></div>
<div class="contact" style="left:280px">
  <svg width="18" height="18" viewBox="0 0 24 24" fill="none" stroke="#fff" stroke-width="2"><path d="M21 10c0 7-9 13-9 13s-9-6-9-13a9 9 0 0 1 18 0z"/><circle cx="12" cy="10" r="3"/></svg>
  <div><small>OUR LOCATION:</small><b>Riverbend, CA</b></div>
</div>

<!-- PARTNERS -->
<div class="partner" style="left:392px">Lumora</div>
<div class="partner" style="left:610px">Veltrax</div>
<div class="partner" style="left:808px">Corvane</div>
<div class="partner" style="left:1045px">Brightpane</div>

<!-- WHY CHOOSE US -->
<div class="ghost" style="left:392px;top:790px;font-size:120px">EXPERIENCE</div>
<h2 style="left:118px;top:862px">Why Choose Us</h2>
<div class="photo" style="left:118px;top:941px;width:303px;height:328px;background:linear-gradient(160deg,#9aa3ab,#4b5158 60%,#a4443e)" role="img" aria-label="Installers applying film to tall windows on ladders"></div>
<div class="photo" style="left:447px;top:941px;width:305px;height:165px;background:linear-gradient(135deg,#3b4a66,#1d2433 55%,#c7b43a)" role="img" aria-label="Installer squeegeeing tint film on a car window"></div>
<div class="photo" style="left:779px;top:941px;width:304px;height:165px;background:linear-gradient(135deg,#d6d8d2,#6f7a66 55%,#2f4a36)" role="img" aria-label="Two installers carrying a glass pane"></div>
<div class="stat" style="left:447px;top:1143px"><div class="num">1200</div><div class="lbl">Windows tinted</div></div>
<div class="stat" style="left:779px;top:1143px"><div class="num">45</div><div class="lbl">Years of experience</div></div>

<!-- SERVICES -->
<svg class="shape" style="top:1372px" width="1200" height="800" aria-hidden="true">
  <polygon points="0,97 1200,0 1200,698 0,795" fill="var(--panel)"/>
</svg>
<div class="ghost" style="left:300px;top:1548px;font-size:110px">SERVICES</div>
<h2 style="left:0;width:1200px;text-align:center;top:1580px">Our Services</h2>
<div class="abs" style="left:118px;top:1708px;font-size:33px;font-weight:400;white-space:nowrap">
  <span class="accent">Residential</span> Tinting</div>
<p class="body" style="left:118px;top:1760px;width:440px">Neque porro quisquam est, qui dolorem ipsum quia dolor sit amet, consectetur, adipisci velit, sed quia non numquam eius modi tempora incidunt ut labore et dolore magnam aliquam quaerat voluptatem. Excepteur sint occaecat cupidatat non proident.</p>
<div class="btn" style="left:118px;top:1868px;width:122px;height:38px">Learn more</div>
<div class="photo" style="left:610px;top:1670px;width:306px;height:237px;background:linear-gradient(170deg,#e6e4de,#b7b3a8 55%,#4a4a48)" role="img" aria-label="Bright living room with tinted floor-to-ceiling windows"></div>
<div class="photo" style="left:942px;top:1670px;width:258px;height:237px;border-radius:4px 0 0 4px;background:linear-gradient(160deg,#a9c6e4,#3f6fa6 55%,#223a5e)" role="img" aria-label="Blue glass office towers"></div>
<div class="abs" style="left:610px;top:1938px;width:473px;height:1px;background:var(--line)"></div>
<div class="abs" style="left:610px;top:1937px;width:84px;height:3px;background:var(--red)"></div>

<!-- HOW WE WORK -->
<svg class="shape" style="top:2070px" width="1200" height="880" aria-hidden="true">
  <polygon points="0,97 1200,0 1200,743 0,870" fill="var(--ink)"/>
</svg>
<div class="ghost" style="left:735px;top:2290px;font-size:110px">WORK</div>
<h2 style="left:100px;top:2384px;font-size:36px">How We <span class="accent">Work</span></h2>
<p class="body" style="left:100px;top:2436px;width:360px">Lorem ipsum dolor sit amet, consectetur adipiscing elit, sed do eiusmod tempor incididunt ut labore et dolore magna aliqua. Ut enim ad minim veniam, quis nostrud exercitation ullamco laboris nisi ut aliquip ex ea commodo consequat. Duis aute irure dolor in reprehenderit in voluptate velit esse cillum dolore eu fugiat nulla pariatur. Excepteur sint occaecat cupidatat non proident, sunt in culpa qui officia.</p>
<div class="photo" style="left:620px;top:2375px;width:440px;height:202px;background:linear-gradient(135deg,#2a2b2e,#6d6f74 45%,#c9cacd)" role="img" aria-label="Close-up of a white car's tinted side window and mirror"></div>
<svg class="abs" style="left:764px;top:2452px" width="46" height="46" viewBox="0 0 46 46" aria-label="Play video" role="img">
  <circle cx="23" cy="23" r="21" fill="var(--red)" stroke="#fff" stroke-width="2"/>
  <polygon points="19,15 31,23 19,31" fill="#fff"/>
</svg>
<div class="feature" style="left:253px"><div class="ic"><svg width="18" height="18" viewBox="0 0 24 24" fill="none" stroke="#fff" stroke-width="2"><path d="M20.6 13.4 13.4 20.6a2 2 0 0 1-2.8 0L3 13V3h10l7.6 7.6a2 2 0 0 1 0 2.8z"/><circle cx="7.5" cy="7.5" r="1.2"/></svg></div><span>Lifetime warranty</span></div>
<div class="feature" style="left:580px"><div class="ic"><svg width="18" height="18" viewBox="0 0 24 24" fill="none" stroke="#fff" stroke-width="2"><path d="M12 2v20M17 6H9.5a3.5 3.5 0 0 0 0 7h5a3.5 3.5 0 0 1 0 7H6"/></svg></div><span>Money-back guarantee</span></div>
<div class="feature" style="left:909px"><div class="ic"><svg width="18" height="18" viewBox="0 0 24 24" fill="none" stroke="#fff" stroke-width="2"><circle cx="12" cy="8" r="6"/><path d="M8.2 13 7 22l5-3 5 3-1.2-9"/></svg></div><span>Licensed installers</span></div>

<!-- SELECTED WORKS -->
<div class="abs" style="left:0;top:2940px;width:1200px;height:828px;background:var(--panel)"></div>
<svg class="shape" style="top:2813px" width="1200" height="128" aria-hidden="true">
  <polygon points="0,128 1200,0 1200,128" fill="var(--panel)"/>
</svg>
<h2 style="left:0;width:1200px;text-align:center;top:3020px;font-size:36px"><span class="accent">Selected</span> Works</h2>
<p class="body" style="left:0;width:1200px;text-align:center;top:3072px;font-size:11px;line-height:1.7">Lorem ipsum dolor sit amet, consetetur sadipscing elitr, sed<br>diam nonumy eirmod tempor invidunt ut labore et dolore magna</p>
<div class="tabs"><span class="on">Show all</span><span>Residential</span><span>Commercial</span><span>Automotive</span></div>
<div class="photo" style="left:118px;top:3197px;width:469px;height:194px;overflow:hidden;background:linear-gradient(160deg,#b6c3cc,#5e7280 55%,#3b4a53)" role="img" aria-label="Glass storefront with tinted panels">
  <div style="position:absolute;left:0;bottom:0;width:100%;height:60px;background:linear-gradient(0deg,rgba(200,16,46,.9),rgba(200,16,46,.5))"></div>
  <div style="position:absolute;left:18px;bottom:22px;font-size:11px">2022 | Harbor Market</div>
  <div style="position:absolute;left:18px;bottom:10px;font-size:8px;color:#f3d1d6">Los Angeles, CA</div>
</div>
<div class="photo" style="left:613px;top:3197px;width:223px;height:194px;background:linear-gradient(170deg,#c9b8a5,#8e8f93 55%,#4d4e52)" role="img" aria-label="Silver sedan in front of mountains"></div>
<div class="photo" style="left:862px;top:3197px;width:221px;height:194px;background:linear-gradient(160deg,#e4e3df,#b89b76 55%,#6e5a44)" role="img" aria-label="Interior room with tinted windows and snowy view"></div>
<div class="photo" style="left:118px;top:3414px;width:223px;height:195px;background:linear-gradient(170deg,#e0a46a,#3e6d8e 60%,#1c3a52)" role="img" aria-label="Blue sports car at sunset"></div>
<div class="photo" style="left:367px;top:3414px;width:220px;height:195px;background:linear-gradient(170deg,#cfd3d4,#7b8a90 55%,#3b3f40)" role="img" aria-label="Room with tinted windows overlooking the sea"></div>
<div class="photo" style="left:613px;top:3414px;width:470px;height:195px;background:linear-gradient(160deg,#a6c4dc,#55758d 55%,#2c3c3a)" role="img" aria-label="Glass office building with palm trees"></div>

<!-- CTA -->
<div class="abs" style="left:0;top:3768px;width:1200px;height:137px;background:var(--red)"></div>
<div class="abs" style="left:118px;top:3820px;font-size:27px;font-weight:400">Want a free personalized quote?</div>
<div class="btn outline" style="left:964px;top:3820px;width:119px;height:34px">Contact us</div>

<!-- HAPPY CUSTOMERS -->
<h2 style="left:118px;top:4018px;font-size:36px"><span class="accent">Happy</span> Customers</h2>
<p class="body" style="left:118px;top:4066px;width:300px;font-size:11px">Lorem ipsum dolor sit amet, consetetur sadipscing elitr, sed diam nonumy eirmod tempor invidunt ut.</p>
<div class="btn" style="left:118px;top:4140px;width:122px;height:36px">See more</div>

<div class="review" style="left:798px;top:4006px">
  <div class="stars">★★★★★</div>
  <q>Lorem ipsum dolor sit amet, consetetur sadipscing elitr, sed diam nonumy eirmod tempor invidunt ut labore et dolore magna aliquyam erat, sed diam voluptua. At vero</q>
  <hr><div class="who"><span class="av" role="img" aria-label="Customer portrait"></span><div><b>Dana Morrow</b><small>Los Angeles, CA</small></div></div>
</div>
<div class="review" style="left:485px;top:4133px">
  <div class="stars">★★★★★</div>
  <q>Lorem ipsum dolor sit amet, consetetur sadipscing elitr, sed diam nonumy eirmod tempor invidunt ut labore et dolore magna aliquyam erat, sed diam voluptua. At vero</q>
  <hr><div class="who"><span class="av" role="img" aria-label="Customer portrait"></span><div><b>Eli Navarro</b><small>Riverbend, CA</small></div></div>
</div>
<div class="review" style="left:798px;top:4260px">
  <div class="stars">★★★★★</div>
  <q>Lorem ipsum dolor sit amet, consetetur sadipscing elitr, sed diam nonumy eirmod tempor invidunt ut labore et dolore magna aliquyam erat, sed diam voluptua. At vero</q>
  <hr><div class="who"><span class="av" role="img" aria-label="Customer portrait"></span><div><b>Ruth Calder</b><small>Burbank, CA</small></div></div>
</div>

<!-- FOOTER -->
<div class="abs" style="left:0;top:4598px;width:1200px;height:342px;background:var(--panel)"></div>
<div class="brand" style="left:118px;top:4672px"><span class="dot"></span>Nova Shade Tinting</div>
<p class="body" style="left:118px;top:4730px;width:300px;font-size:11px;color:var(--white)">Lorem ipsum dolor sit amet, consectetur adipiscing elit, sed do eiusmod tempor incididunt ut labore et dolore magna aliqua.</p>
<div class="social" style="left:118px"><svg width="14" height="14" viewBox="0 0 24 24" fill="var(--red)"><circle cx="12" cy="12" r="6"/></svg></div>
<div class="social" style="left:172px"><svg width="14" height="14" viewBox="0 0 24 24" fill="var(--red)"><rect x="6" y="6" width="12" height="12" rx="2"/></svg></div>
<div class="social" style="left:226px"><svg width="14" height="14" viewBox="0 0 24 24" fill="var(--red)"><circle cx="12" cy="12" r="6"/></svg></div>
<div class="social" style="left:280px"><svg width="14" height="14" viewBox="0 0 24 24" fill="var(--red)"><rect x="6" y="6" width="12" height="12" rx="2"/></svg></div>
<div class="social" style="left:334px"><svg width="16" height="16" viewBox="0 0 24 24" fill="none" stroke="var(--red)" stroke-width="2.4"><path d="M22 16.9v3a2 2 0 0 1-2.2 2 19.8 19.8 0 0 1-8.6-3.1 19.5 19.5 0 0 1-6-6A19.8 19.8 0 0 1 2.1 4.2 2 2 0 0 1 4.1 2h3a2 2 0 0 1 2 1.7c.1 1 .4 1.9.7 2.8a2 2 0 0 1-.5 2.1L8 9.9a16 16 0 0 0 6 6l1.3-1.3a2 2 0 0 1 2.1-.4c.9.3 1.8.6 2.8.7a2 2 0 0 1 1.7 2z"/></svg></div>

<div class="fcol abs" style="left:696px;top:4688px">
  <h4>Services</h4><a>Automotive Tinting</a><a>Commercial Tinting</a><a>Residential Tinting</a>
</div>
<div class="fcol abs" style="left:944px;top:4688px">
  <h4>Resources</h4><a>About us</a><a>Blog</a><a>FAQs</a>
</div>

<div class="abs" style="left:0;top:4940px;width:1200px;height:60px;background:var(--red)"></div>
<div class="abs" style="left:118px;top:4963px;font-size:9px">© 2023 Nova Shade Tinting. All Rights Reserved.</div>
<div class="abs" style="left:843px;top:4963px;font-size:9px">Privacy Policy</div>
<div class="abs" style="left:1000px;top:4963px;font-size:9px">Terms of Service</div>

</body>
</html>
```